Brenfield Chiropractic Business Cards

[Front]
[KLV/Stormrider LOGO & Brenfield Chiropractic LOGO]
Neck & Back Pain Relief
Dr. Martin Pavely
Doctor of Chiropractic

• Short Term Care For Your Neck & Back Pain
• No Referral Needed
• Affordable / Insurance Accepted
• Proficient in treating Soft Tissue Problems

[Back]
For Valuable Wellness Letter Bulletins™ Emailed To You Free, Go To:
www.DrMartinPavelyJournal.example
[SpinaVault LOGO] - can be small

OFFICE HOURS:
Monday – Thursday
9 am - 12 noon, 2 pm - 6 pm
WALK-INS WELCOME

Industry/Entity Type

Business

Contact Information for Business Card

Brenfield Chiropractic Center, PLLC
4837 Tarrow Avenue, Suite K
Hollisford, NC 28999
(252) 555-0147
www.brenfieldchiro.example

Requirements
Must have
• The KLV/Stormrider Logo
The Brenfield Chiropractic Logo
Should not have
• A picture of a spine

```html
<!DOCTYPE html>
<html lang="en">
<head>
<meta charset="utf-8">
<title>Brenfield Chiropractic Business Card</title>
<link rel="stylesheet" href="https://fonts.googleapis.com/css2?family=Sorts+Mill+Goudy&display=swap">
<style>
  :root {
    --page-bg: #2b2b2d;
    --card-bg: #ffffff;
    --ink: #1f1f24;
    --navy: #2e2a86;
    --teal: #2aa3bd;
    --teal-mid: #7fcadb;
    --teal-light: #e3f3f7;
    --brand-red: #d8262e;
    --brand-blue: #1e4fa0;
  }
  * { box-sizing: border-box; margin: 0; padding: 0; }
  html, body {
    width: 1200px; height: 758px; overflow: hidden;
    background: var(--page-bg);
    font-family: "Sorts Mill Goudy", "Georgia", serif;
    color: var(--ink);
  }
  .card {
    position: absolute; left: 80px; top: 82px;
    width: 1040px; height: 594px;
    background: var(--card-bg);
    overflow: hidden;
  }
  .card-wave { position: absolute; inset: 0; }
  .brand {
    position: absolute; left: 44px; top: 92px;
    display: flex; align-items: center; gap: 14px;
    font-size: 40px; letter-spacing: 2px; font-variant: small-caps;
    color: var(--ink);
  }
  .brand-dot {
    width: 30px; height: 30px; border-radius: 50%;
    background: var(--navy);
  }
  .doctor {
    position: absolute; right: 44px; top: 38px;
    text-align: right; font-size: 25px; line-height: 1.22;
  }
  .benefits {
    position: absolute; left: 470px; top: 178px;
    list-style: none; font-size: 23px; line-height: 1.36;
  }
  .benefits li::before { content: "•"; margin-right: 10px; }
  .address {
    position: absolute; left: 64px; top: 272px;
    font-size: 25px; line-height: 1.38; font-style: normal;
  }
  .address span { display: block; }
  .address .indent-1 { padding-left: 10px; }
  .address .indent-2 { padding-left: 20px; }
  .address .indent-3 { padding-left: 30px; }
  .partners {
    position: absolute; left: 40px; bottom: 30px;
    display: flex; align-items: center; gap: 22px;
    font-size: 28px;
  }
  .partner-klv { color: var(--brand-red); }
  .partner-storm { color: var(--brand-blue); }
  .partner-divider { width: 1px; height: 34px; background: var(--brand-blue); }
</style>
</head>
<body>
  <section class="card" aria-label="Brenfield Chiropractic business card">
    <svg class="card-wave" viewBox="0 0 1040 594" preserveAspectRatio="none" aria-hidden="true">
      <defs>
        <linearGradient id="tealFade" x1="0" y1="0" x2="1" y2="0">
          <stop offset="0" stop-color="var(--teal-light)" stop-opacity="0.6"/>
          <stop offset="0.45" stop-color="var(--teal-mid)"/>
          <stop offset="1" stop-color="var(--teal)"/>
        </linearGradient>
      </defs>
      <path class="wave-fill" d="M0 300 C 120 400, 250 470, 360 480 C 450 502, 540 512, 640 504 C 800 490, 930 390, 1040 340 L1040 594 L0 594 Z" fill="url(#tealFade)"/>
      <path class="wave-stroke" d="M340 476 C 450 494, 560 496, 640 488 C 800 472, 930 372, 1040 318 L1040 340 C 930 390, 800 490, 640 504 C 540 512, 450 502, 340 476 Z" fill="var(--navy)"/>
    </svg>

    <div class="brand"><span class="brand-dot"></span>Brenfield Chiropractic</div>

    <div class="doctor">
      <p>Neck &amp; Back Pain Relief</p>
      <p>Dr. Martin Pavely</p>
      <p>Doctor of Chiropractic</p>
    </div>

    <ul class="benefits">
      <li>Short Term Care For Your Neck &amp; Back Pain</li>
      <li>No Referral Needed</li>
      <li>Affordable / Insurance Accepted</li>
      <li>Proficient in treating Soft Tissue Problems</li>
    </ul>

    <address class="address">
      <span>Brenfield Chiropractic Center,</span>
      <span class="indent-1">PLLC 4837 Tarrow Avenue,</span>
      <span class="indent-1">Suite K Hollisford,</span>
      <span class="indent-2">NC 28999 (252) 555-0147</span>
      <span class="indent-3">www.brenfieldchiro.example</span>
    </address>

    <div class="partners">
      <span class="partner-klv">KLV</span>
      <span class="partner-divider"></span>
      <span class="partner-storm">Stormrider</span>
    </div>
  </section>
</body>
</html>
```